Tolvik cards

I want a simple business card that pops.
Logo on one side.
On side two i want.
"Are you thinking about a new building on your property, or renovating an existing structure? Contact".....
Owners Name: Gary Pellman
Owners Phone number: 555-209-4176
Address:4716 Copper Fern RD, Marlow Springs, PA 16940
Committed to Quality, Service, and Integrity

```html
<!DOCTYPE html>
<html lang="en">
<head>
<meta charset="utf-8">
<title>Tolvik Builders LLC — Business Card</title>
<link rel="stylesheet" href="https://fonts.googleapis.com/css2?family=Poppins:wght@300;400;600;800&display=swap">
<style>
  :root {
    --stage: #1d1d1f;
    --brown: #412d1e;
    --brown-soft: #6b5140;
    --paper: #ffffff;
    --ink-light: #ffffff;
  }
  * { box-sizing: border-box; margin: 0; padding: 0; }
  html, body {
    width: 1200px; height: 1200px; overflow: hidden;
    background: var(--stage);
    font-family: "Poppins", sans-serif;
  }
  .stage {
    width: 1200px; height: 1200px;
    display: flex; flex-direction: column; align-items: center; justify-content: center;
    gap: 40px;
  }
  .card {
    width: 880px; height: 503px; position: relative;
    box-shadow: 0 14px 30px rgba(0,0,0,.45);
  }
  .card-front {
    background: var(--brown); color: var(--ink-light);
    display: flex; flex-direction: column; align-items: center; justify-content: center;
  }
  .brand-mark { display: flex; align-items: center; gap: 22px; }
  .brand-square { width: 56px; height: 56px; background: var(--ink-light); }
  .brand-lockup { text-align: center; line-height: 1; font-weight: 800; }
  .brand-name { font-size: 104px; letter-spacing: 2px; }
  .brand-sub { font-size: 30px; letter-spacing: 3px; margin-top: 6px; }
  .tagline {
    margin-top: 34px; font-weight: 300; font-size: 21px;
    letter-spacing: 4px; text-transform: uppercase;
  }
  .card-back {
    background: var(--paper); color: var(--brown);
    padding: 46px 70px 40px;
    display: flex; flex-direction: column; align-items: center;
  }
  .card-back .brand-name { font-size: 96px; }
  .card-back .brand-sub { font-size: 28px; }
  .pitch {
    margin-top: 18px; text-align: center; font-weight: 600;
    font-size: 21px; line-height: 1.3; text-transform: uppercase; letter-spacing: .5px;
  }
  .contact {
    margin-top: 26px; width: 100%;
    display: flex; align-items: center; justify-content: center; gap: 40px;
  }
  .owner-name { font-weight: 600; font-size: 26px; text-transform: uppercase; letter-spacing: .5px; }
  .divider { width: 2px; height: 104px; background: var(--brown); }
  .address { font-weight: 400; font-size: 23px; line-height: 1.3; }
  .phone { display: flex; align-items: center; gap: 10px; }
  .phone-icon { width: 22px; height: 22px; }
</style>
</head>
<body>
<main class="stage">
  <section class="card card-front">
    <div class="brand-mark">
      <div class="brand-square"></div>
      <div class="brand-lockup">
        <div class="brand-name">TOLVIK</div>
        <div class="brand-sub">BUILDERS LLC</div>
      </div>
    </div>
    <p class="tagline">Committed to quality | service | and integrity</p>
  </section>

  <section class="card card-back">
    <div class="brand-lockup">
      <div class="brand-name">TOLVIK</div>
      <div class="brand-sub">BUILDERS LLC</div>
    </div>
    <p class="pitch">Are you thinking<br>about a new building on your property,<br>or renovating an<br>existing structure? Contact</p>
    <div class="contact">
      <p class="owner-name">Gary Pellman</p>
      <div class="divider"></div>
      <div class="address">
        <p>4716 Copper Fern RD,</p>
        <p>Marlow Springs, PA 16940</p>
        <p class="phone">
          <svg class="phone-icon" viewBox="0 0 24 24" aria-hidden="true">
            <circle cx="12" cy="12" r="12" fill="var(--brown-soft)"/>
            <path d="M9 6.5c.6 0 1 .5 1.2 1.6l.3 1.3c.1.5-.1.9-.5 1.2l-.7.5c.6 1.5 1.6 2.6 3 3.3l.6-.7c.3-.4.8-.5 1.2-.4l1.3.4c1 .3 1.4.7 1.3 1.3-.2 1.4-1.3 2.5-2.7 2.3C9.6 17 6.9 14 6.5 10.1 6.4 8 7.6 6.5 9 6.5z" fill="#fff"/>
          </svg>
          555-209-4176
        </p>
      </div>
    </div>
  </section>
</main>
</body>
</html>
```